We are looking for an effective ad to recruit work from home Loan Officers for our Mortgage Brokerage.
Use the following text...
Earn Mortgage Income in your sleep. Its as easy as 1, 2, 3.....
1) Solicit Potential Applicants (Word of Mouth, Email, Social Media etc.)
2) Take Complete Applications & Submit Them
3) Wait to Get Paid.......(Avg. $2,500 per closing)
"You open the door, we'll finish the deal"
No Experience Necessary
No Goals or Quotas
No Office Hours / Work from Home Office
...and We Fully Reimburse ALL LICENSING FEES!!
Email Resume to mwelby@brightharborloans.example
Bright Harbor Lending Group, Inc.
947 W Caldwell Avenue, #318
Baltimore, MD 21230
NMLS #731860
www.brightharborloans.example
Phone (800) 555-0142
Licensed Mortgage Broker in MD and DC since 1997
Target Market(s)
Professionals looking to earn part time income at Loan Officers, preferably with strong social media following.
Industry/Entity Type
Loan
Look and feel

```html
<!DOCTYPE html>
<html lang="en">
<head>
<meta charset="utf-8">
<title>Loan Officer Recruitment Flyer</title>
<link rel="stylesheet" href="https://fonts.googleapis.com/css2?family=Anton&family=Open+Sans:wght@400;600&family=Saira+Semi+Condensed:wght@500&family=Montserrat:wght@700&display=swap">
<style>
  :root {
    --stage: #1c1c1c;
    --blue-light: #2460b4;
    --blue-mid: #14469a;
    --blue-deep: #0b2c70;
    --yellow: #f8c400;
    --gold-band: #ae9a2b;
    --white: #ffffff;
    --navy-text: #1b3e8c;
    --tick: #d2b21c;
  }
  html, body { margin: 0; padding: 0; width: 1200px; height: 1200px; overflow: hidden; background: var(--stage); }
  .flyer { position: absolute; left: 160px; top: 30px; width: 880px; height: 1140px; display: block; }
  .headline { font-family: "Anton", "Impact", sans-serif; fill: var(--white); }
  .licensed { font-family: "Open Sans", sans-serif; font-size: 15px; fill: var(--white); }
  .easy { font-family: "Anton", "Impact", sans-serif; font-size: 44px; fill: var(--yellow); }
  .step-num { font-family: "Anton", "Impact", sans-serif; font-size: 56px; fill: var(--white); }
  .step-text { font-family: "Saira Semi Condensed", "Arial Narrow", sans-serif; font-weight: 500; font-size: 27px; fill: var(--white); }
  .perk { font-family: "Open Sans", sans-serif; font-weight: 600; font-size: 15.5px; fill: var(--yellow); }
  .reimburse { font-family: "Montserrat", sans-serif; font-weight: 700; font-size: 20px; fill: var(--white); letter-spacing: 1px; }
  .slogan { font-family: "Anton", "Impact", sans-serif; font-size: 34px; fill: var(--yellow); }
  .footer-text { font-family: "Saira Semi Condensed", "Arial Narrow", sans-serif; font-weight: 500; fill: var(--white); }
  .brand-name { font-family: "Saira Semi Condensed", "Arial Narrow", sans-serif; font-weight: 500; fill: var(--navy-text); }
  .social-name { font-family: "Saira Semi Condensed", "Arial Narrow", sans-serif; font-weight: 500; fill: var(--navy-text); }
</style>
</head>
<body>
<svg class="flyer" viewBox="0 0 845 1095" xmlns="http://www.w3.org/2000/svg">
  <defs>
    <linearGradient id="panelBlue" x1="0" y1="0" x2="1" y2="1">
      <stop offset="0" stop-color="var(--blue-light)"/>
      <stop offset="0.55" stop-color="var(--blue-mid)"/>
      <stop offset="1" stop-color="var(--blue-deep)"/>
    </linearGradient>
    <radialGradient id="coinGold" cx="0.4" cy="0.3" r="0.75">
      <stop offset="0" stop-color="#ffe066"/>
      <stop offset="0.6" stop-color="#e8a412"/>
      <stop offset="1" stop-color="#b56a05"/>
    </radialGradient>
    <linearGradient id="photoShade" x1="0" y1="0" x2="1" y2="1">
      <stop offset="0" stop-color="#1c4fa2" stop-opacity="0"/>
      <stop offset="1" stop-color="#3b6fb0" stop-opacity="0.35"/>
    </linearGradient>
  </defs>

  <!-- main panel -->
  <rect class="panel" x="0" y="0" width="845" height="972" fill="url(#panelBlue)"/>
  <rect class="photo-area" x="0" y="380" width="845" height="400" fill="url(#photoShade)" role="img" aria-label="Faint photo of a hand over dollar bills"/>

  <!-- brand box -->
  <rect class="brand-box" x="534" y="0" width="311" height="327" fill="var(--white)"/>
  <circle cx="600" cy="163" r="12" fill="var(--navy-text)"/>
  <text class="brand-name" x="620" y="157" font-size="20">Bright Harbor</text>
  <text class="brand-name" x="620" y="181" font-size="20">Lending Group, Inc.</text>
  <text class="brand-name" x="689" y="218" font-size="11" text-anchor="middle">"You open the door, we'll finish the deal"</text>

  <!-- headline -->
  <text class="licensed" x="502" y="40" text-anchor="end">Licensed Mortgage Broker in MD and DC since 1997</text>
  <text class="headline" x="72" y="113" font-size="62" textLength="430" lengthAdjust="spacingAndGlyphs">EARN MORTGAGE</text>
  <text class="headline" x="70" y="245" font-size="130" textLength="434" lengthAdjust="spacingAndGlyphs">INCOME</text>
  <text class="headline" x="72" y="327" font-size="69" textLength="428" lengthAdjust="spacingAndGlyphs">IN YOUR SLEEP</text>

  <text class="easy" x="433" y="411" text-anchor="middle" textLength="506" lengthAdjust="spacingAndGlyphs">.....it's As EASY As 1, 2, 3.....</text>

  <!-- steps -->
  <g class="step">
    <circle cx="165" cy="473" r="41" fill="url(#coinGold)"/>
    <text class="step-num" x="165" y="495" text-anchor="middle">1</text>
    <text class="step-text" x="229" y="467" textLength="310" lengthAdjust="spacingAndGlyphs">Solicit Potential Applicants</text>
    <text class="step-text" x="229" y="501" textLength="476" lengthAdjust="spacingAndGlyphs">(Word of Mouth, Email, Social Media etc.)</text>
  </g>
  <g class="step">
    <circle cx="165" cy="568" r="41" fill="url(#coinGold)"/>
    <text class="step-num" x="165" y="590" text-anchor="middle">2</text>
    <text class="step-text" x="229" y="582" textLength="503" lengthAdjust="spacingAndGlyphs">Take Complete Applications &amp; Submit Them</text>
  </g>
  <g class="step">
    <circle cx="165" cy="664" r="41" fill="url(#coinGold)"/>
    <text class="step-num" x="165" y="686" text-anchor="middle">3</text>
    <text class="step-text" x="229" y="672" textLength="490" lengthAdjust="spacingAndGlyphs">Wait to Get Paid (Avg. $2,500 per closing)</text>
  </g>

  <!-- social badge -->
  <rect class="social-badge" x="76" y="736" width="412" height="120" rx="8" fill="var(--white)" stroke="#c9d3e6" stroke-width="3"/>
  <rect x="92" y="754" width="84" height="84" rx="10" fill="var(--navy-text)"/>
  <text class="social-name" x="330" y="775" font-size="24" text-anchor="middle">LIKE US ON</text>
  <text class="social-name" x="330" y="832" font-size="50" text-anchor="middle">Friendloop</text>

  <!-- perks -->
  <g class="perks" fill="none" stroke="var(--tick)" stroke-width="2.5" stroke-linecap="round">
    <path d="M520 768 l6 7 l14 -16"/>
    <path d="M520 796 l6 7 l14 -16"/>
    <path d="M520 823 l6 7 l14 -16"/>
  </g>
  <text class="perk" x="552" y="771">NO EXPERIENCE NECESSARY</text>
  <text class="perk" x="551" y="798">NO GOALS OR QUOTAS</text>
  <text class="perk" x="549" y="825">NO OFFICE HOURS / WORK</text>
  <text class="perk" x="549" y="845">FROM HOME OFFICE</text>

  <text class="reimburse" x="422" y="902" text-anchor="middle">...AND WE FULLY REIMBURSE ALL LICENSING FEES!!</text>
  <text class="slogan" x="422" y="951" text-anchor="middle" textLength="632" lengthAdjust="spacingAndGlyphs">"YOU OPEN THE DOOR WE'LL FINISH THE DEAL"</text>

  <!-- footer -->
  <rect class="footer-band" x="0" y="972" width="845" height="123" fill="var(--gold-band)"/>
  <g class="pin-icon">
    <path d="M63 991 a26 26 0 0 1 26 26 c0 20 -26 46 -26 46 c0 0 -26 -26 -26 -46 a26 26 0 0 1 26 -26z" fill="var(--white)"/>
    <circle cx="63" cy="1017" r="10" fill="var(--gold-band)"/>
    <circle cx="63" cy="1017" r="5" fill="var(--white)"/>
  </g>
  <text class="footer-text" x="101" y="1006" font-size="14" textLength="214" lengthAdjust="spacingAndGlyphs">Bright Harbor Lending Group, Inc.</text>
  <text class="footer-text" x="101" y="1026" font-size="14">947 W Caldwell Avenue, #318</text>
  <text class="footer-text" x="101" y="1046" font-size="14">Baltimore, MD 21230</text>
  <text class="footer-text" x="101" y="1066" font-size="14">NMLS #731860</text>

  <g class="phone-icon">
    <circle cx="366" cy="1006" r="19" fill="none" stroke="var(--white)" stroke-width="3"/>
    <path d="M358 997 c-3 6 2 16 12 20 l4 -4 l-5 -4 l-3 2 c-3 -2 -5 -4 -6 -7 l2 -3 l-3 -5z" fill="var(--white)"/>
  </g>
  <text class="footer-text" x="396" y="1018" font-size="32">(800) 555-0142</text>

  <g class="mail-icon" fill="none" stroke="var(--white)" stroke-width="2.5">
    <rect x="348" y="1043" width="28" height="19"/>
    <path d="M348 1043 l14 10 l14 -10"/>
  </g>
  <text class="footer-text" x="383" y="1057" font-size="13" textLength="205" lengthAdjust="spacingAndGlyphs">mwelby@brightharborloans.example</text>

  <g class="globe-icon" fill="none" stroke="var(--white)" stroke-width="2">
    <circle cx="614" cy="1052" r="12"/>
    <ellipse cx="614" cy="1052" rx="5.5" ry="12"/>
    <path d="M602 1052 h24"/>
  </g>
  <text class="footer-text" x="634" y="1057" font-size="13" textLength="192" lengthAdjust="spacingAndGlyphs">www.brightharborloans.example</text>
</svg>
</body>
</html>
```